Business Card Design

Need to have a business card recreated. The layout of the card needs to remain the same and it must be easy to update the information on the card. If needed, I can try to get better copies of the logos but the last printer did not give us any files.

```html
<!DOCTYPE html>
<html lang="en">
<head>
<meta charset="utf-8">
<title>Keystone Surgical Centers – Business Card</title>
<link href="https://fonts.googleapis.com/css2?family=Questrial&family=Montserrat:wght@700&family=Tinos&display=swap" rel="stylesheet">
<style>
  :root{
    --bg:#d9d9d9;
    --paper:#f8f8fa;
    --brand-blue:#1f4fa3;
    --navy:#0c1e45;
    --ink:#15213f;
    --white:#ffffff;
    --tile-cyan:#2bd1f7;
    --tile-lime:#9bc552;
    --tile-teal:#00737a;
    --tile-aqua:#00c2b2;
    --tile-blue:#0067b1;
    --tile-red:#f3354b;
  }
  *{box-sizing:border-box;margin:0;padding:0}
  html,body{width:1200px;height:1200px;overflow:hidden;background:var(--bg)}
  .sheet{position:relative;width:1200px;height:1200px}
  .card{position:absolute;left:150px;width:900px;height:514px;overflow:hidden;
        box-shadow:0 10px 28px rgba(0,0,0,.18)}
  .card--front{top:50px;background:var(--paper)}
  .card--back{top:636px;display:grid;grid-template-columns:repeat(3,1fr);grid-template-rows:repeat(2,1fr)}

  /* front */
  .front-wave{position:absolute;inset:0;width:900px;height:514px}
  .holder{position:absolute;left:64px;top:150px}
  .holder__name{font-family:"Questrial",sans-serif;font-size:50px;color:var(--brand-blue);line-height:1}
  .holder__title{font-family:"Questrial",sans-serif;font-size:17px;color:var(--ink);margin-top:10px}
  .contact-list{list-style:none;margin-top:38px}
  .contact-list li{display:flex;align-items:center;gap:14px;font-family:"Questrial",sans-serif;
                   font-size:18px;color:var(--brand-blue);margin-bottom:14px}
  .contact-icon{width:32px;height:32px;border-radius:50%;background:var(--brand-blue);
                display:flex;align-items:center;justify-content:center}
  .brand{position:absolute;right:70px;top:110px;text-align:left}
  .brand__name{display:flex;align-items:center;gap:12px;font-family:"Montserrat",sans-serif;
               font-weight:700;font-size:52px;color:var(--brand-blue);line-height:1}
  .brand__mark{width:22px;height:22px;background:var(--brand-blue)}

  /* back */
  .tile{display:flex;flex-direction:column;align-items:center;justify-content:center;
        text-align:center;color:var(--white);padding:20px}
  .tile--cyan{background:var(--tile-cyan)}
  .tile--lime{background:var(--tile-lime)}
  .tile--teal{background:var(--tile-teal)}
  .tile--aqua{background:var(--tile-aqua)}
  .tile--blue{background:var(--tile-blue)}
  .tile--red{background:var(--tile-red)}
  .tile__name{font-family:"Montserrat",sans-serif;font-weight:700;font-size:22px;line-height:1.15;
              display:flex;align-items:center;gap:8px;margin-bottom:18px}
  .tile__mark{width:12px;height:12px;background:var(--white);flex:none}
  .tile__address{font-family:"Tinos",serif;font-size:17px;line-height:1.3;margin-bottom:18px}
  .tile__phone{display:flex;align-items:center;gap:10px;font-family:"Tinos",serif;font-size:17px}
</style>
</head>
<body>
<main class="sheet">

  <section class="card card--front" aria-label="Front side">
    <svg class="front-wave" viewBox="0 0 900 514" aria-hidden="true">
      <path d="M0 352 C180 368 330 380 470 330 C560 298 610 250 660 232 C560 290 500 350 380 380 C250 410 120 400 0 388 Z" fill="var(--brand-blue)"/>
      <path d="M0 410 C160 420 330 430 470 385 C600 342 660 270 720 255 C790 238 850 250 900 262 L900 514 L0 514 Z" fill="var(--navy)"/>
    </svg>

    <div class="brand">
      <div class="brand__name"><span class="brand__mark"></span>Keystone</div>
      <div class="brand__name" style="font-size:19px;margin-top:8px;color:var(--ink)">Surgical Centers</div>
    </div>

    <div class="holder">
      <h1 class="holder__name">Dana Whitlock</h1>
      <p class="holder__title">Director of Marketing</p>
      <ul class="contact-list">
        <li>
          <span class="contact-icon">
            <svg width="16" height="16" viewBox="0 0 24 24"><path d="M6.6 10.8a15 15 0 0 0 6.6 6.6l2.2-2.2a1 1 0 0 1 1-.25 11.4 11.4 0 0 0 3.6.57 1 1 0 0 1 1 1V20a1 1 0 0 1-1 1A17 17 0 0 1 3 4a1 1 0 0 1 1-1h3.5a1 1 0 0 1 1 1c0 1.25.2 2.45.57 3.57a1 1 0 0 1-.25 1z" fill="#fff"/></svg>
          </span>555.014.2288
        </li>
        <li>
          <span class="contact-icon">
            <svg width="16" height="16" viewBox="0 0 24 24"><rect x="3" y="6" width="18" height="12" rx="1.5" fill="#fff"/><path d="M3.5 7l8.5 6 8.5-6" stroke="var(--brand-blue)" stroke-width="1.8" fill="none"/></svg>
          </span>dana@keystonecaregroup.com
        </li>
      </ul>
    </div>
  </section>

  <section class="card card--back" aria-label="Back side">
    <article class="tile tile--cyan">
      <h2 class="tile__name"><span class="tile__mark"></span>Keystone</h2>
      <p class="tile__address">12 Harbor St.<br>Maple Ridge, NJ 07001</p>
      <p class="tile__phone"><svg width="22" height="22" viewBox="0 0 24 24"><circle cx="12" cy="12" r="10" stroke="#fff" stroke-width="1.8" fill="none"/><path d="M8.5 8.5c.6 3.3 3.7 6.4 7 7l1-1.5-2-1-1 .8c-1-.5-2-1.5-2.4-2.4l.8-1-1-2z" fill="#fff"/></svg>555.201.3344</p>
    </article>
    <article class="tile tile--lime">
      <h2 class="tile__name">Bright Vale<br>Surgical Center</h2>
      <p class="tile__address">48 Linden Ave., Suite 200<br>Oakmont, NJ 07002</p>
      <p class="tile__phone"><svg width="22" height="22" viewBox="0 0 24 24"><circle cx="12" cy="12" r="10" stroke="#fff" stroke-width="1.8" fill="none"/><path d="M8.5 8.5c.6 3.3 3.7 6.4 7 7l1-1.5-2-1-1 .8c-1-.5-2-1.5-2.4-2.4l.8-1-1-2z" fill="#fff"/></svg>555.318.4402</p>
    </article>
    <article class="tile tile--teal">
      <h2 class="tile__name">Park Row<br>Surgery Center</h2>
      <p class="tile__address">210 Park Row<br>Eastfield, NY 10001</p>
      <p class="tile__phone"><svg width="22" height="22" viewBox="0 0 24 24"><circle cx="12" cy="12" r="10" stroke="#fff" stroke-width="1.8" fill="none"/><path d="M8.5 8.5c.6 3.3 3.7 6.4 7 7l1-1.5-2-1-1 .8c-1-.5-2-1.5-2.4-2.4l.8-1-1-2z" fill="#fff"/></svg>555.402.7781</p>
    </article>
    <article class="tile tile--aqua">
      <h2 class="tile__name"><span class="tile__mark"></span>Keystone</h2>
      <p class="tile__address">75 River Rd. 4th Floor<br>Harbor City, NJ 07003</p>
      <p class="tile__phone"><svg width="22" height="22" viewBox="0 0 24 24"><circle cx="12" cy="12" r="10" stroke="#fff" stroke-width="1.8" fill="none"/><path d="M8.5 8.5c.6 3.3 3.7 6.4 7 7l1-1.5-2-1-1 .8c-1-.5-2-1.5-2.4-2.4l.8-1-1-2z" fill="#fff"/></svg>555.611.0925</p>
    </article>
    <article class="tile tile--blue">
      <h2 class="tile__name"><span class="tile__mark" style="border-radius:50%"></span>Eastbank<br>Surgery Center</h2>
      <p class="tile__address">900 Elm Ave.<br>Eastbank, NY 10002</p>
      <p class="tile__phone"><svg width="22" height="22" viewBox="0 0 24 24"><circle cx="12" cy="12" r="10" stroke="#fff" stroke-width="1.8" fill="none"/><path d="M8.5 8.5c.6 3.3 3.7 6.4 7 7l1-1.5-2-1-1 .8c-1-.5-2-1.5-2.4-2.4l.8-1-1-2z" fill="#fff"/></svg>555.733.4409</p>
    </article>
    <article class="tile tile--red">
      <h2 class="tile__name">Lakeshore<br>Surgery Center</h2>
      <p class="tile__address">30 Mill Ln, Suite 101<br>Fairhaven, NJ 07004</p>
      <p class="tile__phone"><svg width="22" height="22" viewBox="0 0 24 24"><circle cx="12" cy="12" r="10" stroke="#fff" stroke-width="1.8" fill="none"/><path d="M8.5 8.5c.6 3.3 3.7 6.4 7 7l1-1.5-2-1-1 .8c-1-.5-2-1.5-2.4-2.4l.8-1-1-2z" fill="#fff"/></svg>555.820.5990</p>
    </article>
  </section>

</main>
</body>
</html>
```